Korvanta Brochure Design - IT Services - Modern Design - Services List

Hi,

We are looking for a modern IT Services brochure design of between 4 - 6 pages, it must be based on a blue and white colour theme with some nice technical imagery. It would need a section about why Korvanta and a contact section at the end.

Here is some info that could be included

Target Market(s)

Medium to Large Businesses

Industry/Entity Type

Information Technology

Colors
0054AA
0677BA
7BADD7
CADEEF
E8F1F8

Requirements
Must have
• Striking technical imagery
Nice to have
• Nice Icons to list the different services sections

```html
<!DOCTYPE html>
<html lang="en">
<head>
<meta charset="utf-8">
<title>Korvanta – IT Services Brochure 2025</title>
<link href="https://fonts.googleapis.com/css2?family=Lexend:wght@300;400;600;700&family=Montserrat:wght@400;500;600;700&display=swap" rel="stylesheet">
<style>
:root{
  --navy:#0c4767;
  --blue:#0b92d0;
  --blue-deep:#0677ba;
  --sky:#7badd7;
  --mist:#cadeef;
  --ice:#e8f1f8;
  --ink:#1c2530;
  --white:#ffffff;
  --head:"Lexend",sans-serif;
  --body:"Montserrat",sans-serif;
}
*{margin:0;padding:0;box-sizing:border-box}
html,body{width:1200px;height:3000px;overflow:hidden;background:#fff}
body{position:relative;font-family:var(--body);color:var(--ink)}
.page{position:absolute;width:422px;height:601px;background:#fff;overflow:hidden;box-shadow:0 0 6px rgba(0,0,0,.28)}
.page>svg.bg{position:absolute;left:0;top:0;width:422px;height:601px}
.abs{position:absolute}
.col-l{left:76px}.col-r{left:703px}
.row-1{top:152px}.row-2{top:846px}.row-3{top:1540px}.row-4{top:2234px}
.h-light{font-family:var(--head);font-weight:400;line-height:1}
.h-bold{font-family:var(--head);font-weight:700;line-height:1}
.body-text{font-size:8.6px;line-height:1.42;color:var(--ink)}
.justify{text-align:justify}
.item{position:absolute;width:150px}
.item .bar{width:36px;height:4px;background:var(--navy);margin-bottom:4px}
.item .bar.blue{background:var(--blue)}
.item h4{font-size:8.4px;font-weight:700;color:var(--ink);line-height:1.25}
.item p{font-size:8.4px;line-height:1.3;color:var(--ink)}
.photo{position:absolute}
/* cover */
.brand-name{font-family:var(--head);font-weight:700;font-size:22px;color:var(--blue);letter-spacing:.5px}
.cover-contact{font-size:5.5px;line-height:1.35;color:var(--navy)}
.empower{color:#fff;font-family:var(--head);font-weight:600;line-height:.95}
.year{font-family:var(--head);font-weight:700;font-size:40px;color:#fff;-webkit-text-stroke:1.6px var(--blue)}
.contact-line{font-size:9px;color:#fff;line-height:1.35}
.icon-dot{width:13px;height:13px;border-radius:50%;background:#fff;display:flex;align-items:center;justify-content:center}
.why h3{font-family:var(--head);font-weight:600;font-size:15px;line-height:1;}
.why p{font-size:8.3px;line-height:1.42;text-align:justify}
</style>
</head>
<body>

<!-- Back page: contact -->
<section class="page col-l row-1 contact-page">
  <svg class="bg" viewBox="0 0 422 601">
    <rect x="0" y="355" width="422" height="143" fill="var(--navy)"/>
    <polygon points="422,420 422,498 320,498 355,440 380,420" fill="#fff"/>
    <polygon points="422,432 422,498 388,498" fill="var(--blue)"/>
    <rect x="0" y="518" width="422" height="3" fill="var(--blue)"/>
  </svg>
  <h1 class="abs h-bold" style="left:93px;top:118px;font-size:25px;font-weight:600;color:var(--blue)">Get in Touch</h1>
  <p class="abs body-text" style="left:95px;top:180px;width:178px;font-size:8.5px">Discover how Korvanta can transform your IT landscape and drive your business forward.<br>Contact us today to learn more about our services and how we can help you achieve your goals.</p>
  <h2 class="abs h-bold" style="left:56px;top:380px;font-size:16px;color:var(--blue)">Contact Us</h2>
  <div class="abs" style="left:56px;top:400px;width:30px;height:2px;background:var(--blue)"></div>
  <div class="abs icon-dot" style="left:56px;top:429px"><svg width="8" height="8" viewBox="0 0 24 24"><path d="M6 2l4 4-2 3c1 3 4 6 7 7l3-2 4 4-3 4C10 21 3 14 2 5z" fill="var(--navy)"/></svg></div>
  <div class="abs contact-line" style="left:83px;top:429px">+44 161 555 0148</div>
  <div class="abs contact-line" style="left:81px;top:450px">48 Meridian Row,<br>Harbour Park,<br>London, UK</div>
  <div class="abs icon-dot" style="left:198px;top:429px"><svg width="9" height="9" viewBox="0 0 24 24" fill="none" stroke="var(--navy)" stroke-width="2.4"><circle cx="12" cy="12" r="9"/><path d="M3 12h18M12 3c3 3 3 15 0 18M12 3c-3 3-3 15 0 18"/></svg></div>
  <div class="abs contact-line" style="left:223px;top:425px">www.korvanta.co.uk<br>info@korvanta.co.uk</div>
</section>

<!-- Front cover -->
<section class="page col-r row-1 cover-page">
  <svg class="bg" viewBox="0 0 422 601">
    <defs>
      <linearGradient id="cityGlow" x1="0" y1="0" x2="1" y2="1">
        <stop offset="0" stop-color="#c9d6e6"/><stop offset=".5" stop-color="#4d6a93"/><stop offset="1" stop-color="#1a2e52"/>
      </linearGradient>
    </defs>
    <polygon points="85,104 112,104 40,245 24,228" fill="var(--blue)"/>
    <polygon points="200,104 330,104 350,118 345,140 385,160 300,345 50,345 32,318 112,150" fill="var(--navy)"/>
    <polygon points="115,104 300,104 355,160 285,345 50,345 32,318" fill="url(#cityGlow)" role="img" aria-label="Night city skyline with light trails on a highway"/>
    <rect x="70" y="332" width="296" height="3" fill="var(--blue)"/>
    <polygon points="0,356 105,356 80,420 0,420" fill="var(--navy)"/>
    <polygon points="122,356 320,356 270,498 0,498 0,432 92,432" fill="var(--blue)"/>
    <polygon points="108,370 130,356 100,432 86,432" fill="#fff"/>
    <polygon points="378,313 422,313 422,345 385,405 298,405 330,378 350,378" fill="var(--navy)"/>
    <rect x="0" y="518" width="235" height="3" fill="var(--blue)"/>
  </svg>
  <div class="abs brand-name" style="left:90px;top:40px">Korvanta</div>
  <div class="abs" style="left:256px;top:42px;width:2px;height:27px;background:var(--navy)"></div>
  <div class="abs cover-contact" style="left:272px;top:40px">
    <div>● +44 161 555 0148</div>
    <div style="margin-top:9px">● www.korvanta.co.uk<br>&nbsp;&nbsp;&nbsp;info@korvanta.co.uk</div>
  </div>
  <div class="abs empower" style="left:110px;top:392px;font-size:24px">EMPOWERING</div>
  <div class="abs empower" style="left:110px;top:413px;font-size:19px;font-weight:400">YOUR BUSINESS</div>
  <div class="abs empower" style="left:110px;top:431px;font-size:7.5px;font-weight:400">WITH CUTTING-EDGE IT SOLUTIONS</div>
  <div class="abs year" style="left:253px;top:496px">2025</div>
</section>

<!-- About -->
<section class="page col-l row-2 about-page">
  <svg class="bg" viewBox="0 0 422 601">
    <defs>
      <radialGradient id="cloudCity" cx=".5" cy=".55" r=".6">
        <stop offset="0" stop-color="#7fd4ff"/><stop offset=".5" stop-color="#1f5fb8"/><stop offset="1" stop-color="#0a1c3f"/>
      </radialGradient>
    </defs>
    <path d="M0 60 H422 V107 H385 C360 107 355 135 345 160 H0 Z" fill="var(--navy)"/>
    <rect x="35" y="168" width="175" height="150" rx="14" fill="#2f4d68" role="img" aria-label="Hand drawing on a digital IT and data interface"/>
    <circle cx="131" cy="371" r="88" fill="var(--navy)"/>
    <circle cx="131" cy="371" r="74" fill="url(#cloudCity)" role="img" aria-label="Glowing digital city under a cloud icon"/>
  </svg>
  <div class="abs h-light" style="left:219px;top:119px;font-size:23px;color:#fff">About</div>
  <div class="abs h-bold" style="left:219px;top:142px;font-size:23px;color:#fff">Korvanta</div>
  <p class="abs body-text justify" style="left:230px;top:213px;width:145px;font-size:10px;line-height:1.44">At Korvanta, we are dedicated to providing top-tier IT services that drive efficiency, innovation, and growth for your business. With a commitment to excellence and a team of highly skilled professionals, we offer a comprehensive suite of solutions tailored to meet the unique needs of our clients.</p>
</section>

<!-- Managed IT services -->
<section class="page col-r row-2 services-page">
  <svg class="bg" viewBox="0 0 422 601">
    <polygon points="0,0 422,0 422,75 345,75 370,0 160,0 125,75 0,75" fill="var(--navy)"/>
    <polygon points="160,0 370,0 345,75 330,110 115,110" fill="var(--blue)"/>
    <polygon points="0,75 40,75 20,110 0,110" fill="var(--blue)"/>
    <polygon points="40,75 125,75 115,110 20,110" fill="#fff"/>
    <rect x="34" y="467" width="330" height="2.5" fill="var(--blue)"/>
    <rect x="34" y="533" width="330" height="2.5" fill="var(--blue)"/>
    <!-- icons -->
    <g fill="none" stroke="var(--blue-deep)" stroke-width="1.3">
      <circle cx="58" cy="257" r="8"/><path d="M50 257h16M58 249c4 3 4 13 0 16M58 249c-4 3-4 13 0 16"/>
      <rect x="38" y="268" width="14" height="10"/><rect x="65" y="268" width="14" height="10"/><path d="M58 265v8M45 273h27"/>
      <rect x="42" y="390" width="26" height="18" rx="1"/><circle cx="55" cy="399" r="5"/><path d="M50 412h10"/>
      <circle cx="244" cy="386" r="4"/><circle cx="233" cy="403" r="4"/><circle cx="244" cy="403" r="4"/><circle cx="255" cy="403" r="4"/><path d="M244 390v9M233 397h22"/>
    </g>
    <g fill="var(--navy)">
      <path d="M232 262a12 12 0 0 1 24 0v6h-4v-6a8 8 0 0 0-16 0v6h-4z"/>
      <rect x="228" y="276" width="32" height="10" rx="4"/>
    </g>
  </svg>
  <div class="abs h-light" style="left:39px;top:125px;font-size:23px;color:var(--ink)">Our Services</div>
  <div class="abs h-bold" style="left:39px;top:149px;font-size:24px;color:var(--ink)">Managed IT Services</div>
  <p class="abs body-text justify" style="left:39px;top:200px;width:326px;font-size:9.6px">Our Managed IT Services provide proactive monitoring and management of your IT infrastructure, ensuring maximum uptime and reliability. We offer:</p>
  <div class="item" style="left:38px;top:283px;width:145px"><div class="bar blue"></div><h4>24/7 Network Monitoring:</h4><p>Continuous monitoring to detect and resolve issues before they impact your business.</p></div>
  <div class="item" style="left:227px;top:283px;width:142px"><div class="bar blue"></div><h4>Helpdesk Support:</h4><p>Responsive and knowledgeable support team available round the clock.</p></div>
  <div class="item" style="left:38px;top:421px;width:145px"><div class="bar blue"></div><h4>Patch Management:</h4><p>Regular updates and patches to keep your systems secure and up-to-date.</p></div>
  <div class="item" style="left:227px;top:421px;width:142px"><div class="bar blue"></div><h4>IT Asset Management:</h4><p>Comprehensive tracking and management of your IT assets.</p></div>
</section>

<!-- Cloud -->
<section class="page col-l row-3 cloud-page">
  <svg class="bg" viewBox="0 0 422 601">
    <polygon points="0,443 290,443 265,500 0,500" fill="var(--navy)"/>
    <polygon points="140,300 422,300 422,343 370,443 0,443 0,378 110,378" fill="var(--blue)"/>
    <polygon points="0,295 422,295 422,300 0,300" fill="var(--navy)" opacity="0"/>
    <polygon points="388,443 422,375 422,443" fill="var(--navy)"/>
    <path d="M422 450 C405 455 395 470 400 480 C405 490 415 492 422 490 Z" fill="#c07a68" role="img" aria-label="Cropped photo of a hand"/>
  </svg>
  <div class="abs h-light" style="left:59px;top:52px;font-size:23px;color:var(--blue)">Cloud</div>
  <div class="abs h-bold" style="left:59px;top:74px;font-size:23px;color:var(--navy)">Solutions</div>
  <p class="abs body-text" style="left:59px;top:108px;width:300px;font-size:8.3px">Embrace the power of the cloud with our scalable and secure cloud solutions. Our offerings include:</p>
  <div class="item" style="left:56px;top:143px"><div class="bar"></div><h4>Cloud Migration:</h4><p class="justify">Seamless transition of your applications and data to the cloud.</p></div>
  <div class="item" style="left:245px;top:143px"><div class="bar"></div><h4>Cloud Hosting:</h4><p class="justify">Reliable and scalable hosting solutions to meet your growing needs.</p></div>
  <div class="item" style="left:56px;top:230px"><div class="bar blue"></div><h4>Backup and Disaster Recovery:</h4><p class="justify">Robust backup and recovery solutions to ensure business continuity.</p></div>
  <div class="item" style="left:245px;top:230px"><div class="bar blue"></div><h4>Software as a Service (SaaS):</h4><p class="justify">Access to the latest software applications without the hassle of maintenance.</p></div>
  <div class="abs h-light" style="left:166px;top:326px;font-size:42px;color:#fff;font-weight:600">Cloud</div>
  <div class="abs h-light" style="left:166px;top:366px;font-size:42px;color:transparent;-webkit-text-stroke:1.4px #fff;font-weight:600">Solutions</div>
</section>

<!-- Cybersecurity -->
<section class="page col-r row-3 cyber-page">
  <svg class="bg" viewBox="0 0 422 601">
    <defs>
      <linearGradient id="cyberGlow" x1="0" y1="0" x2="1" y2="0">
        <stop offset="0" stop-color="#1c2c45"/><stop offset=".5" stop-color="#2c6aa8"/><stop offset="1" stop-color="#0d2244"/>
      </linearGradient>
    </defs>
    <polygon points="0,292 65,292 30,338 0,338" fill="var(--blue)"/>
    <polygon points="248,292 422,292 422,338 215,338" fill="var(--navy)"/>
    <path d="M0 300 H90 C105 300 110 340 140 340 H422 V543 H170 C150 543 140 520 110 520 H0 Z" fill="url(#cyberGlow)" role="img" aria-label="Hands using a laptop under glowing cybersecurity network icons"/>
  </svg>
  <div class="abs h-bold" style="left:38px;top:72px;font-size:24px;font-weight:600;color:var(--navy)">Cybersecurity</div>
  <p class="abs body-text" style="left:38px;top:103px;width:300px;font-size:8.3px">Protect your business from evolving threats with our comprehensive cybersecurity services. We offer:</p>
  <div class="item" style="left:35px;top:131px;width:145px"><div class="bar blue"></div><h4>Threat Detection and Response:</h4><p>Advanced threat monitoring and response to safeguard your data.</p></div>
  <div class="item" style="left:224px;top:131px;width:150px"><div class="bar blue"></div><h4>Security Audits and Assessments:</h4><p>Thorough evaluations to identify and mitigate vulnerabilities.</p></div>
  <div class="item" style="left:35px;top:219px;width:145px"><div class="bar"></div><h4>Endpoint Protection:</h4><p>Robust security solutions for all your devices.</p></div>
  <div class="item" style="left:224px;top:219px;width:150px"><div class="bar"></div><h4>Compliance and Regulatory Services:</h4><p>Ensure adherence to industry standards and regulations.</p></div>
</section>

<!-- IT Consulting -->
<section class="page col-l row-4 consulting-page">
  <svg class="bg" viewBox="0 0 422 601">
    <defs>
      <linearGradient id="officeTone" x1="0" y1="0" x2="1" y2="1">
        <stop offset="0" stop-color="#c9d4dc"/><stop offset=".55" stop-color="#7f95a8"/><stop offset="1" stop-color="#3f5468"/>
      </linearGradient>
    </defs>
    <rect x="0" y="0" width="422" height="338" fill="url(#officeTone)" role="img" aria-label="Two businessmen reviewing work on a laptop in an office"/>
    <path d="M422 120 C380 125 365 150 365 190 C365 230 330 240 300 240 H270 L250 255 H422 Z" fill="var(--navy)"/>
    <path d="M0 246 H170 C200 246 220 300 260 338 H0 Z" fill="var(--blue)"/>
    <path d="M260 338 C300 338 330 300 360 290 C390 280 410 285 422 285 V338 Z" fill="#fff"/>
  </svg>
  <div class="abs h-light" style="left:35px;top:284px;font-size:20px;color:#fff">IT</div>
  <div class="abs h-bold" style="left:35px;top:303px;font-size:23px;font-weight:600;color:#fff">Consulting</div>
  <p class="abs body-text" style="left:60px;top:355px;width:310px;font-size:8.3px">Leverage our expertise to drive your IT strategy and achieve your business goals. Our consulting services include:</p>
  <div class="item" style="left:58px;top:408px;width:140px"><div class="bar"></div><h4>IT Strategy and Planning:</h4><p>Strategic guidance to align your IT initiatives with your business objectives.</p></div>
  <div class="item" style="left:246px;top:408px;width:140px"><div class="bar"></div><h4>Technology Assessments:</h4><p>In-depth evaluations to optimize your IT infrastructure.</p></div>
  <div class="item" style="left:58px;top:495px;width:140px"><div class="bar blue"></div><h4>Project Management:</h4><p class="justify">Expert management of IT projects from inception to completion.</p></div>
  <div class="item" style="left:246px;top:495px;width:140px"><div class="bar blue"></div><h4>Business Continuity Planning:</h4><p class="justify">Strategies to ensure your business remains operational during disruptions.</p></div>
</section>

<!-- Why choose -->
<section class="page col-r row-4 why-page">
  <svg class="bg" viewBox="0 0 422 601">
    <rect x="10" y="0" width="412" height="245" fill="var(--navy)"/>
    <rect x="0" y="245" width="422" height="88" fill="var(--navy)"/>
    <path d="M0 245 H150 L110 333 H0 Z" fill="var(--blue)"/>
    <path d="M110 333 H150 C185 333 190 265 220 265 C250 265 245 333 285 333 Z" fill="#fff"/>
  </svg>
  <div class="why abs" style="left:45px;top:46px;width:145px;color:#fff"><h3>Proactive<br>Support</h3><p style="margin-top:13px">Our proactive support model ensures that potential issues are identified and resolved before they can impact your operations. We are committed to maintaining the highest levels of service availability and performance.</p></div>
  <div class="why abs" style="left:236px;top:46px;width:143px;color:#fff"><h3>Comprehensive<br>Solutions</h3><p style="margin-top:13px">From managed services to cybersecurity, we offer a comprehensive suite of IT solutions designed to meet the diverse needs of your business. Our holistic approach ensures that all aspects of your IT infrastructure are covered.</p></div>
  <div class="abs h-bold" style="right:45px;top:223px;font-size:21px;font-weight:600;color:var(--blue);text-align:right">Why Choose</div>
  <div class="abs h-bold" style="right:45px;top:245px;font-size:22px;font-weight:600;color:transparent;-webkit-text-stroke:1.1px #fff;text-align:right">KORVANTA?</div>
  <div class="why abs" style="left:45px;top:368px;width:142px;color:var(--ink)"><h3 style="color:var(--blue-deep)">Expertise and<br>Experience</h3><p style="margin-top:13px">With years of experience in the IT industry, our team possesses the knowledge and skills to tackle any challenge. We stay abreast of the latest technological advancements to provide you with cutting-edge solutions.</p></div>
  <div class="why abs" style="left:236px;top:368px;width:143px;color:var(--ink)"><h3 style="color:var(--blue-deep)">Customer-Centric<br>Approach</h3><p style="margin-top:13px">We prioritize our clients' needs and work closely with them to deliver customized solutions that drive success. Our client-centric approach ensures that we are always aligned with your business goals.</p></div>
</section>

</body>
</html>
```